German Auto Restoration Website Design

We are working with a Classic Car Restoration company in California.
They compete with guys like this:
https://brackenmotorworks.com

We could not find any auto restoration company websites for inspiration. We attached some images of the type of work they do.

Thank you for taking the time to consider designing a website for us. We are web developers based in Stockton, CA, USA. Most of our projects go through the same process. Understanding this process may help you win a project with us. We custom-code all of our websites in-house. We don’t have any requirements as to what tools you use for your design, but we ask that you follow these guidelines.

IMAGES:
If you use any images or icons in the design, we ask that you have a link to the asset so we can purchase the image/icon. Most of the designs we submit do not have the customer’s images on them unless they have some great images. Be creative; show us the feeling you are trying to portray with your image choices. Use any royalty-free site you choose. We subscribe to Quillon and mainly use their images, but we can purchase images outside of Quillon. PLEASE NOTE: we will not submit designs to clients with watermarks on the images.

FONTS:
We ask that you identify the fonts you’re using in the design. This can be done in a message if you want. We typically use Vantrel Fonts and Quillon Fonts.

CONTENT:
We're always open to different content and ideas. We often submit designs with stock images so the client can see our vision. We typically take pictures after the website launch to use their images with our vision. Lorem Ipsum is fine for paragraphs, but we ask that you make the Headers with correct English. We want to be able to show the vision and identify the sections of the website.

INSPIRATION:
We typically add a couple of links in the brief of websites we like to help you get started in your design.

REVISIONS:
We do not often ask for revisions of the designs unless we see something in the design that may not appeal to the client. If there are slight changes that we want to make, we do that in the development process.

FEEDBACK:
We rarely give feedback on designs during the design process. We are working on many website projects and do not have the time to provide feedback. We usually respond if your request is well thought out and asks specific questions, but a note asking “feedback, please” usually goes unanswered.

```html
<!DOCTYPE html>
<html lang="en">
<head>
<meta charset="utf-8">
<title>Kessler Restorations — Classic Car Restoration</title>
<link rel="stylesheet" href="https://fonts.googleapis.com/css2?family=Urbanist:wght@500;600;700;800&family=Poppins:wght@400;500;600&display=swap">
<style>
:root{
  --red:#e31e24;
  --ink:#111111;
  --text:#555555;
  --muted:#8a8a8a;
  --line:#e2e2e2;
  --band:#f6f6f6;
  --white:#ffffff;
  --yellow:#f6c900;
}
*{box-sizing:border-box;margin:0;padding:0}
html,body{width:1200px;height:4552px;overflow:hidden}
body{position:relative;background:var(--white);font-family:"Poppins",sans-serif;color:var(--text)}
.abs{position:absolute}
h1,h2,.stat-num{font-family:"Urbanist",sans-serif;color:var(--ink);font-weight:800;letter-spacing:-0.5px}
.accent{color:var(--red)}
.brand{display:flex;align-items:center;gap:10px;font-family:"Poppins",sans-serif;font-weight:600;color:var(--ink);letter-spacing:2px;font-size:13px;white-space:nowrap}
.brand-dot{width:12px;height:12px;background:var(--red);border-radius:50%}
.nav{font-size:12px;color:var(--ink)}
.nav span{position:absolute;white-space:nowrap}
.btn{display:inline-flex;align-items:center;justify-content:center;gap:6px;background:var(--red);color:var(--white);font-size:12px;font-weight:500;border-radius:8px;height:38px;padding:0 20px;white-space:nowrap}
.btn svg{width:11px;height:11px}
p.body{font-size:11.5px;line-height:27px}
.center{left:0;width:1200px;text-align:center}
.section-title{font-size:37px;line-height:1}
.stat-num{font-size:36px;font-weight:600}
.stat-label{font-size:12px;color:var(--ink);white-space:nowrap}
.divider{width:1px;height:72px;background:var(--line)}
.service-card{background:var(--white);border-radius:14px;box-shadow:0 4px 18px rgba(0,0,0,.06);text-align:center}
.service-icon{position:absolute;left:50%;top:46px;width:74px;height:74px;margin-left:-37px;border-radius:50%;display:flex;align-items:center;justify-content:center}
.service-icon.red{background:#fde6e6}
.service-icon.yellow{background:#fff6d6}
.service-name{position:absolute;left:0;right:0;top:146px;font-size:18px;line-height:27px;color:var(--ink);font-weight:500}
.caption{position:absolute;left:21px;font-size:12px;line-height:27px;color:var(--white);white-space:nowrap}
.blog-card{background:var(--white);border-radius:10px;box-shadow:0 4px 18px rgba(0,0,0,.08);overflow:hidden}
.blog-title{position:absolute;left:21px;top:241px;font-size:12.5px;line-height:27px;font-weight:500;color:var(--ink);white-space:nowrap}
.blog-meta{position:absolute;left:21px;top:311px;font-size:11px;color:var(--muted);font-style:italic;display:flex;align-items:center;gap:16px}
.blog-meta i{width:7px;height:7px;background:var(--red);border-radius:50%;display:block}
.field{position:absolute;left:32px;width:339px;border:1px solid var(--line);border-radius:6px;font-size:10px;color:#aaa;padding:14px}
.info-row{position:absolute;left:106px;display:flex;align-items:center;gap:15px;font-size:13px;font-weight:500;color:var(--ink);white-space:nowrap}
.social{width:14px;height:14px;border-radius:50%;background:var(--ink)}
</style>
</head>
<body>

<header>
  <div class="abs brand" style="left:106px;top:28px"><span class="brand-dot"></span>KESSLER RESTORATIONS</div>
  <nav class="nav abs" style="top:30px;left:0;width:1200px">
    <span style="left:689px">Home</span><span style="left:754px">About</span><span style="left:822px">Services</span><span style="left:903px">Portfolio</span><span style="left:984px">Blog</span><span style="left:1039px">Contact</span>
  </nav>
</header>

<section class="hero">
  <h1 class="abs" style="left:106px;top:142px;font-size:38px;line-height:53px">We Specialize In <span class="accent">Restoring</span><br>&amp; Preserving Vintage Cars<br>To Their <span class="accent">Original Beauty.</span></h1>
  <p class="abs body" style="left:106px;top:315px;width:560px">Lorem Ipsum Dolor Sit Amet Consectetur. Lorem Ut Quam Nulla Dolor.<br>Rhoncus Lectus Maecenas Eget Platea Malesuada Pharetrau. Venenatis.</p>
  <a class="abs btn" style="left:106px;top:397px">Book A Free Service <svg viewBox="0 0 12 12"><path d="M1 6h9M6.5 2.5 10 6l-3.5 3.5" stroke="#fff" stroke-width="1.6" fill="none"/></svg></a>
  <div class="abs" role="img" aria-label="Black vintage coupe sports car, three-quarter front view" style="left:648px;top:240px;width:552px;height:290px;background:radial-gradient(ellipse at 50% 60%,#2a2a2a 0%,#3e3e3e 45%,rgba(255,255,255,0) 72%)"></div>
</section>

<section class="stats">
  <div class="abs" style="left:111px;top:540px"><div class="stat-num">25+</div><div class="stat-label" style="margin-top:6px">Year Experience</div></div>
  <div class="abs divider" style="left:302px;top:546px"></div>
  <div class="abs" style="left:383px;top:540px"><div class="stat-num">100%</div><div class="stat-label" style="margin-top:6px">Facility Capabilities</div></div>
  <div class="abs divider" style="left:595px;top:546px"></div>
  <div class="abs" style="left:677px;top:540px"><div class="stat-num">1500+</div><div class="stat-label" style="margin-top:6px">Car Restoration Done</div></div>
  <div class="abs divider" style="left:903px;top:546px"></div>
  <div class="abs" style="left:986px;top:540px"><div class="stat-num">500+</div><div class="stat-label" style="margin-top:6px">Happy Clients</div></div>
</section>

<section class="about">
  <div class="abs" role="img" aria-label="Silver vintage compact car with luggage rack, side view" style="left:0;top:716px;width:583px;height:318px;background:radial-gradient(ellipse at 50% 62%,#cfcfcf 0%,#e6e6e6 45%,rgba(255,255,255,0) 72%)"></div>
  <h2 class="abs section-title" style="left:689px;top:761px"><span class="accent">Know</span> Who We Are</h2>
  <p class="abs body" style="left:689px;top:812px;width:405px">Lorem Ipsum Dolor Sit Amet Consectetur. Lorem Ut Quam Nulla Dolor. Rhoncus Lectus Maecenas Eget Platea Malesuada Pharetra Quis A Enim. Elit Iaculis Nullam Ornare Habitasse. Et Nulla Cras Tellus Dignissim Ut. Ullamcorper Quisque Nec In In Nunc Eget Dolor Vitae Arcu. Venenatis.</p>
  <a class="abs btn" style="left:689px;top:962px">Book A Free Service <svg viewBox="0 0 12 12"><path d="M1 6h9M6.5 2.5 10 6l-3.5 3.5" stroke="#fff" stroke-width="1.6" fill="none"/></svg></a>
</section>

<section class="process">
  <h2 class="abs section-title" style="left:106px;top:1205px"><span class="accent">See</span> Our Process</h2>
  <p class="abs body" style="left:106px;top:1256px;width:400px">Lorem Ipsum Dolor Sit Amet Consectetur. Lorem Ut Quam<br>Nulla Dolor. Rhoncus Lectus Maecenas Eget Platea<br>Malesuada Pharetra Quis A Enim. Elit Iaculis Nullam.Platea<br>Malesuada Pharetra Quis A Enim. Elit Iaculis Nullam</p>
  <a class="abs btn" style="left:106px;top:1377px">Book A Free Service <svg viewBox="0 0 12 12"><path d="M1 6h9M6.5 2.5 10 6l-3.5 3.5" stroke="#fff" stroke-width="1.6" fill="none"/></svg></a>
  <div class="abs" role="img" aria-label="Video of a mechanic in gloves rebuilding an engine" style="left:620px;top:1138px;width:478px;height:316px;border-radius:10px;background:linear-gradient(135deg,#3a3f44,#1b1d20 60%,#4a4d52)"></div>
  <div class="abs" style="left:576px;top:1456px;width:572px;height:8px;border-radius:0 0 8px 8px;background:linear-gradient(#cfcfcf,#9a9a9a)"></div>
  <svg class="abs" style="left:839px;top:1287px" width="40" height="40" viewBox="0 0 40 40"><circle cx="20" cy="20" r="20" fill="#fff"/><path d="M16 13l11 7-11 7z" fill="#111"/></svg>
</section>

<section class="services">
  <div class="abs" style="left:0;top:1578px;width:1200px;height:498px;background:var(--band)"></div>
  <h2 class="abs section-title center" style="top:1611px"><span class="accent">Services</span> That We Offer</h2>
  <p class="abs body center" style="top:1662px">Lorem Ipsum Dolor Sit Amet Consectetur. Lorem Ut Quam Nulla Dolor. Rhoncus Lectus Maecenas Eget<br>Platea Malesuada Pharetra Quis A Enim. Elit Iaculis Nullam.Platea</p>
  <div class="abs service-card" style="left:106px;top:1755px;width:239px;height:238px">
    <div class="service-icon red"><svg width="30" height="30" viewBox="0 0 30 30" fill="none" stroke="#e31e24" stroke-width="2"><path d="M6 8h18M15 8v12M10 26h10M12 20h6"/></svg></div>
    <div class="service-name">Metal Forming &amp;<br>Fabrication</div>
  </div>
  <div class="abs service-card" style="left:355px;top:1755px;width:239px;height:238px">
    <div class="service-icon yellow"><svg width="30" height="30" viewBox="0 0 30 30" fill="none" stroke="#f0b400" stroke-width="2"><circle cx="15" cy="15" r="9"/><circle cx="15" cy="15" r="3"/></svg></div>
    <div class="service-name">Mechanical<br>Services</div>
  </div>
  <div class="abs service-card" style="left:606px;top:1755px;width:239px;height:238px">
    <div class="service-icon red"><svg width="30" height="30" viewBox="0 0 30 30" fill="none" stroke="#e31e24" stroke-width="2"><path d="M5 20v-5l3-6h14l3 6v5zM8 20v3M22 20v3"/></svg></div>
    <div class="service-name">Accident<br>Restoration</div>
  </div>
  <div class="abs service-card" style="left:855px;top:1755px;width:239px;height:238px">
    <div class="service-icon yellow"><svg width="30" height="30" viewBox="0 0 30 30" fill="none" stroke="#f0b400" stroke-width="2"><rect x="7" y="8" width="16" height="13" rx="2"/><path d="M7 15h16M10 21v3M20 21v3"/></svg></div>
    <div class="service-name">Specialty Renew<br>Vehicles</div>
  </div>
  <svg class="abs" style="left:570px;top:2033px" width="60" height="8"><circle cx="4" cy="4" r="3" fill="#e31e24"/><circle cx="21" cy="4" r="3" fill="#d5d5d5"/><circle cx="38" cy="4" r="3" fill="#d5d5d5"/><circle cx="55" cy="4" r="3" fill="#d5d5d5"/></svg>
</section>

<section class="portfolio">
  <h2 class="abs section-title center" style="top:2164px">Our <span class="accent">Portfolio</span></h2>
  <p class="abs body center" style="top:2215px">Lorem Ipsum Dolor Sit Amet Consectetur. Lorem Ut Quam Nulla Dolor. Rhoncus Lectus Maecenas Eget<br>Platea Malesuada Pharetra Quis A Enim. Elit Iaculis Nullam.Platea</p>
  <div class="abs" role="img" aria-label="Close-up of a black alloy wheel with red brake caliper" style="left:106px;top:2311px;width:488px;height:283px;background:linear-gradient(135deg,#2c2c2c,#6b6b6b 55%,#1e1e1e)">
    <div class="caption" style="top:201px">Lorem Ipsum Dolor Sit Amet Consectetur.<br>Lorem Ut Quam Nulla Dolor.</div>
  </div>
  <div class="abs" role="img" aria-label="Row of restored classic cars under a cloudy sky" style="left:106px;top:2615px;width:488px;height:283px;background:linear-gradient(180deg,#8a96a3,#5c6670 55%,#3a3f45)">
    <div class="caption" style="top:201px">Lorem Ipsum Dolor Sit Amet Consectetur.<br>Lorem Ut Quam Nulla Dolor.</div>
  </div>
  <div class="abs" role="img" aria-label="Cream vintage coupe parked on green grass" style="left:606px;top:2311px;width:488px;height:587px;background:linear-gradient(180deg,#6f9a3e,#b9b7a4 45%,#6f6c60 80%,#3a3a34)">
    <div class="caption" style="top:505px">Lorem Ipsum Dolor Sit Amet Consectetur.<br>Lorem Ut Quam Nulla Dolor.</div>
  </div>
  <a class="abs btn" style="left:501px;top:2944px">Book A Free Service <svg viewBox="0 0 12 12"><path d="M1 6h9M6.5 2.5 10 6l-3.5 3.5" stroke="#fff" stroke-width="1.6" fill="none"/></svg></a>
</section>

<section class="blog">
  <h2 class="abs section-title center" style="top:3074px">Our <span class="accent">Blog</span></h2>
  <p class="abs body center" style="top:3125px">Lorem Ipsum Dolor Sit Amet Consectetur. Lorem Ut Quam Nulla Dolor.<br>Rhoncus Lectus Maecenas Eget Platea</p>
  <article class="abs blog-card" style="left:106px;top:3191px;width:322px;height:348px">
    <div role="img" aria-label="Rusted vintage car in a dim barn" style="height:225px;background:linear-gradient(135deg,#2b221c,#7a4b2c 55%,#231b16)"></div>
    <div class="blog-title">Lorem Ipsum Dolor Sit Amet Consectetur.<br>Lorem Ut Quam Nulla Dolor.</div>
    <div class="blog-meta">15 May 2023 <i></i> Lorem Ipsum</div>
  </article>
  <article class="abs blog-card" style="left:438px;top:3191px;width:324px;height:348px">
    <div role="img" aria-label="Blue classic car being repaired in a workshop" style="height:225px;background:linear-gradient(135deg,#3b2a26,#2f4664 55%,#221c1c)"></div>
    <div class="blog-title">Lorem Ipsum Dolor Sit Amet Consectetur.<br>Lorem Ut Quam Nulla Dolor.</div>
    <div class="blog-meta">15 May 2023 <i></i> Lorem Ipsum</div>
  </article>
  <article class="abs blog-card" style="left:772px;top:3191px;width:322px;height:348px">
    <div role="img" aria-label="Weathered old pickup truck in a garage" style="height:225px;background:linear-gradient(135deg,#4a4640,#8b8478 55%,#3a3631)"></div>
    <div class="blog-title">Lorem Ipsum Dolor Sit Amet Consectetur.<br>Lorem Ut Quam Nulla Dolor.</div>
    <div class="blog-meta">15 May 2023 <i></i> Lorem Ipsum</div>
  </article>
  <a class="abs btn" style="left:501px;top:3584px">Book A Free Service <svg viewBox="0 0 12 12"><path d="M1 6h9M6.5 2.5 10 6l-3.5 3.5" stroke="#fff" stroke-width="1.6" fill="none"/></svg></a>
</section>

<section class="contact">
  <h2 class="abs section-title center" style="top:3714px"><span class="accent">Contact Us</span> To Get A Free Service</h2>
  <p class="abs body center" style="top:3765px">Lorem Ipsum Dolor Sit Amet Consectetur. Quis Aliquam Luctus Netus Habitant Adipiscing In A Commodo. Mattis Mattis Dignissim<br>Neque Pulvinar Id Sodales Mauris. Lorem Tellus In Amet Tellus. Lobortis Etiam Scelerisque Leo.</p>
  <div class="abs" role="img" aria-label="Satellite map of the workshop area" style="left:0;top:3847px;width:590px;height:314px;background:linear-gradient(135deg,#7c7f79,#9a9c94 50%,#6d716b)"></div>

  <div class="info-row" style="top:4199px"><svg width="16" height="18" viewBox="0 0 16 18"><path d="M8 1a6 6 0 0 0-6 6c0 4.5 6 10 6 10s6-5.5 6-10a6 6 0 0 0-6-6z" fill="#e31e24"/><circle cx="8" cy="7" r="2.2" fill="#fff"/></svg>Lorem Ipsum Dolor Sit Amet Consectetur.</div>
  <div class="info-row" style="top:4241px"><svg width="16" height="18" viewBox="0 0 16 18"><rect x="3" y="1" width="10" height="16" rx="2" fill="#e31e24"/><rect x="5" y="3" width="6" height="10" fill="#fff"/></svg>555-014-2290</div>
  <div class="info-row" style="top:4282px"><svg width="16" height="18" viewBox="0 0 16 18"><rect x="0" y="3" width="16" height="12" rx="2" fill="#e31e24"/><path d="M1 4l7 6 7-6" stroke="#fff" stroke-width="1.4" fill="none"/></svg>hello@kesslerrestorations.com</div>

  <form class="abs" style="left:691px;top:3847px;width:403px;height:450px;background:#fff;border-radius:12px;box-shadow:0 4px 22px rgba(0,0,0,.09)">
    <div class="abs" style="left:32px;top:32px;font-size:17px;font-weight:500;color:var(--ink)">Leave A Massage</div>
    <div class="field" style="top:81px;height:44px">Your Name *</div>
    <div class="field" style="top:138px;height:44px">Your Email *</div>
    <div class="field" style="top:194px;height:44px">Your Phone</div>
    <div class="field" style="top:252px;height:117px">Massage</div>
    <span class="abs btn" style="left:32px;top:381px;height:37px;padding:0 24px">Send</span>
  </form>
</section>

<footer>
  <div class="abs" style="left:106px;top:4415px;width:988px;height:1px;background:var(--line)"></div>
  <div class="abs brand" style="left:106px;top:4446px;font-size:14px"><span class="brand-dot"></span>KESSLER RESTORATIONS</div>
  <nav class="nav abs" style="top:4452px;left:0;width:1200px">
    <span style="left:558px">Home</span><span style="left:652px">About</span><span style="left:742px">Services</span><span style="left:852px">Portfolio</span><span style="left:958px">Blog</span><span style="left:1039px">Contact</span>
  </nav>
  <div class="abs" style="left:106px;top:4499px;width:988px;height:1px;background:var(--line)"></div>
  <div class="abs" style="left:106px;top:4520px;font-size:12px;color:var(--ink)">© Copyright 2023 All rights received</div>
  <div class="abs" style="left:998px;top:4522px;display:flex;gap:14px">
    <span class="social"></span><span class="social"></span><span class="social"></span><span class="social"></span>
  </div>
</footer>

</body>
</html>
```